2018 Vision Board Workshop

I need to promote this workshop on both an 8.5x11 sheet and a 5x7 card. I do have a logo that needs to be present. I'd like to stay true to my branded colors. The flyer needs to project the excitement of a new year and the possibilities of what a person can create, produce, explore in their lives by putting it all on a vision board. Creating the vision of what you want will inspire you to achieve your goals and dreams. Looking at your vision board each day will propel you into taking action as you chart your course to achieve what you truly want.
The flyer needs to have the following information:
The workshop date and time - Sat., Jan. 13, 2018, 10:30-1:30
The location is - Atrium 47B, 2864 Birchwood Vale Rd, Colorado Springs, Co 80417
in the FORGE Room
My name and contact information - Mara Vollbeck
Text and voice 303-417-6652
Email - mara@brightwell-daily-craft.com
Website - brightwell-daily-craft.com
The fee is $45. All materials are provided.

My company is called Brightwell Daily Craft. I am a Life Coach, author, speaker and workshop leader.\ I wrote this program, Brightwell Daily Craft to teach concepts and supporting skills for living with more happiness, satisfaction and fulfillment. Thanks for reading this!! Mara

Target Market(s)

Primarily women, educated, motivated, proactive in their own lives and well being

Font styles to use
Other font styles liked:
• I have been using Century Gothic. I'm open to new ideas.

Requirements
Must have
• The Brightwell Daily Craft logo
• The flyer needs to have the following information:
• The workshop date and time - Sat., Jan. 13, 2018, 10:30-1:30
• The location is - Atrium 47B, 2864 Birchwood Vale Rd, Colorado Springs, Co 80417
• in the FORGE Room
• My name and contact information - Mara Vollbeck
• Text and voice 303-417-6652
• Email - mara@brightwell-daily-craft.com
• Website - brightwell-daily-craft.com
• The fee is $45. All materials are provided.
Nice to have
• The Brightwell Daily Craft branded colors in the design
• Images of vision boards

```html
<!DOCTYPE html>
<html lang="en">
<head>
<meta charset="utf-8">
<title>2018 Vision Board Workshop – Brightwell Daily Craft</title>
<link rel="stylesheet" href="https://fonts.googleapis.com/css2?family=Crimson+Pro:wght@500;600;700&display=swap">
<style>
  :root {
    --stage: #e4e4e6;
    --paper: #ffffff;
    --ink: #231f20;
    --brand-green: #7cb82f;
    --brand-green-text: #6aa42a;
    --brand-blue: #3b6fbf;
    --brand-sky: #4a9be0;
    --brand-navy: #2a4f8f;
    --photo-dark: #1f2224;
    --photo-mid: #3a3a3c;
    --skyline: #dfe3e8;
  }
  * { margin: 0; padding: 0; box-sizing: border-box; }
  html, body { width: 1200px; height: 822px; overflow: hidden; background: var(--stage); }
  body { font-family: "Crimson Pro", Georgia, serif; color: var(--ink); }

  .flyer {
    position: absolute; left: 307px; top: 0;
    width: 586px; height: 822px;
    background: var(--paper); overflow: hidden;
  }
  .hero-photo {
    position: absolute; left: 0; top: 0; width: 100%; height: 320px;
    background: radial-gradient(ellipse at 50% 55%, var(--photo-mid) 0%, var(--photo-dark) 75%);
  }
  .skyline {
    position: absolute; left: 0; top: 330px; width: 100%; height: 492px;
    background: linear-gradient(180deg, rgba(255,255,255,1) 0%, var(--skyline) 45%, #eef0f3 100%);
    opacity: .8;
  }
  .wave { position: absolute; left: 0; top: 240px; width: 586px; height: 100px; }

  .brand {
    position: absolute; top: 130px; left: 0; width: 100%;
    display: flex; justify-content: center; align-items: center; gap: 12px;
  }
  .brand-dot { width: 16px; height: 16px; border-radius: 50%; background: var(--brand-blue); }
  .brand-name { font-size: 40px; font-weight: 600; color: var(--brand-green); letter-spacing: .5px; line-height: 1; }
  .program {
    position: absolute; top: 180px; left: 0; width: 100%; text-align: center;
    font-size: 18px; font-weight: 600; color: var(--brand-sky); letter-spacing: 1px; line-height: 1;
  }

  .event > * { position: absolute; left: 0; width: 100%; text-align: center; }
  .headline { top: 362px; font-size: 52px; font-weight: 700; line-height: 1; }
  .subhead { top: 418px; font-size: 42px; font-weight: 500; color: var(--brand-green-text); line-height: 1; letter-spacing: .5px; }
  .time { top: 468px; font-size: 45px; font-weight: 700; line-height: 1; }
  .date {
    top: 509px; left: 130px !important; width: 325px !important; height: 61px;
    background: var(--brand-blue); color: #fff; font-size: 42px; font-weight: 600;
    line-height: 61px; box-shadow: 0 4px 6px rgba(0,0,0,.2);
  }
  .date sup { font-size: 22px; vertical-align: 14px; line-height: 0; }
  .day { top: 578px; font-size: 47px; font-weight: 700; color: var(--brand-green-text); line-height: 1; }
  .venue { top: 624px; font-size: 16px; font-weight: 700; line-height: 1.2; }

  .fee-burst { position: absolute; left: -32px; top: 630px; width: 232px; height: 232px; }
  .fee-text {
    position: absolute; left: 8px; top: 676px; width: 150px;
    color: #fff; text-align: center; transform: rotate(-12deg); line-height: 1;
  }
  .fee-label { font-size: 21px; font-weight: 600; }
  .fee-amount { font-size: 62px; font-weight: 700; }
  .fee-note { font-size: 17px; font-weight: 600; line-height: 1.05; }

  .contact { position: absolute; right: 23px; top: 712px; text-align: right; line-height: 1.2; font-style: normal; }
  .contact-name { font-size: 29px; font-weight: 700; color: var(--brand-navy); line-height: 1.05; }
  .contact-name .surname { color: var(--brand-green-text); }
  .contact-role { font-size: 19px; font-weight: 600; color: var(--brand-green-text); }
  .contact-line { font-size: 16px; font-weight: 500; margin-top: 3px; }
  .contact-line .sep { margin: 0 6px; }
</style>
</head>
<body>
  <main class="flyer">
    <div class="hero-photo" role="img" aria-label="Darkened photo of a smiling family with children"></div>
    <div class="skyline" role="img" aria-label="Faint city skyline background"></div>
    <svg class="wave" viewBox="0 0 586 100" aria-hidden="true">
      <path d="M0,70 C140,18 380,2 586,22 L586,100 L0,100 Z" fill="var(--brand-green)"/>
      <path d="M0,84 C150,44 400,30 586,56 L586,100 L0,100 Z" fill="#ffffff"/>
    </svg>

    <div class="brand">
      <span class="brand-dot"></span>
      <span class="brand-name">Brightwell Daily Craft</span>
    </div>
    <p class="program">2018 Vision Board Workshop</p>

    <section class="event">
      <h1 class="headline">What You Think</h1>
      <p class="subhead">Is What You Create</p>
      <p class="time">10:30 to 1:30</p>
      <p class="date">13<sup>th</sup>-Jan-2018</p>
      <p class="day">Saturday</p>
      <p class="venue">at<br>Atrium 47B, 2864 Birchwood Vale Rd<br>Colorado Springs, Co 80417<br>in the FORGE Room</p>
    </section>

    <svg class="fee-burst" viewBox="-100 -100 200 200" aria-hidden="true">
      <polygon fill="var(--brand-blue)" points="100,0 85,13.4 95.1,30.9 76.6,39 80.9,58.8 60.8,60.8 58.8,80.9 39,76.6 30.9,95.1 13.4,85 0,100 -13.4,85 -30.9,95.1 -39,76.6 -58.8,80.9 -60.8,60.8 -80.9,58.8 -76.6,39 -95.1,30.9 -85,13.4 -100,0 -85,-13.4 -95.1,-30.9 -76.6,-39 -80.9,-58.8 -60.8,-60.8 -58.8,-80.9 -39,-76.6 -30.9,-95.1 -13.4,-85 0,-100 13.4,-85 30.9,-95.1 39,-76.6 58.8,-80.9 60.8,-60.8 80.9,-58.8 76.6,-39 95.1,-30.9 85,-13.4"/>
    </svg>
    <div class="fee-text">
      <p class="fee-label">The fee is</p>
      <p class="fee-amount">$45</p>
      <p class="fee-note">All Materials<br>are Provided.</p>
    </div>

    <address class="contact">
      <p class="contact-name">Mara <span class="surname">Vollbeck</span></p>
      <p class="contact-role">Text and Voice</p>
      <p class="contact-line">303-417-6652<span class="sep">|</span>mara@brightwell-daily-craft.com</p>
      <p class="contact-line">brightwell-daily-craft.com</p>
    </address>
  </main>
</body>
</html>
```